New Alcoholic Spiked Seltzer Line

We need a can design for a line of low calorie alcoholic seltzer. This product is a sparkling water and vodka drink with no sugar added in a slim 12 oz can.

This is a lighter, healthier, alternative to the sugary ready-to-drinks on the market. The product contains only 3 ingredients: Vodka, Water and Natural Flavors. It has only 100 calories but still has 5% alcohol, so you don't need to sacrifice alcohol to cut calories.

This product also does not contain any preservatives.

We want this design to communicate the following objectives to the consumer and in this order:

1. Appetizing product
2.Low calorie
3.Communicate the type of beverage (Spiked Seltzer)

The brand name of the product is VELKA.

The flavor of the product needed to be used for the design is Mango-Orange.

Comparable products are:

www.brisavelfizz.example/
https://www.tarnowbubble.example
https://quellrind.example/

The designs should not infringe or copy the creative directions of the products mentionned above. They are only given so that you can better understand the type of product we are developing.

Target Market(s)

Young Professional women between the ages of 25 and 44

Industry/Entity Type

Product

Colors

Designer to choose colors to be used in the design.

Requirements
Must have
• Design extendibility, meaning it can be adapted for other flavors.
• This is a new category in the market we are targeting, so consumers must easily be able to identify what type of product this is.

```html
<!DOCTYPE html>
<html lang="en">
<head>
<meta charset="utf-8">
<title>VELKA Spiked Seltzer – Can Labels</title>
<link rel="stylesheet" href="https://fonts.googleapis.com/css2?family=Anton&family=Oswald:wght@300;400&family=Roboto+Condensed:wght@400;500&display=swap">
<style>
  :root {
    --page: #ffffff;
    --can-body: #ececec;
    --can-edge: #d9d9d9;
    --ink: #111111;
    --orange: #ff6a0a;
    --mango: #f9a51a;
    --art-tone: #cfcfcf;
  }
  * { margin: 0; padding: 0; box-sizing: border-box; }
  html, body { width: 1200px; height: 1200px; overflow: hidden; background: var(--page); }
  .canvas { position: relative; width: 1200px; height: 1200px; }

  .can {
    position: absolute;
    top: 172px;
    width: 314px;
    height: 924px;
    background: linear-gradient(90deg, var(--can-edge) 0%, var(--can-body) 18%, #f6f6f6 50%, var(--can-body) 82%, var(--can-edge) 100%);
    border-radius: 40px 40px 48px 48px;
  }
  .can--orange { left: 251px; --flavor: var(--orange); }
  .can--mango  { left: 695px; --flavor: var(--mango); }

  .band {
    position: absolute;
    left: 0;
    width: 100%;
    height: 22px;
    background: var(--flavor);
  }
  .band--top { top: 72px; }
  .band--bottom { top: 826px; }

  .scene-art {
    position: absolute;
    left: 13px;
    top: 128px;
    width: 288px;
    height: 250px;
    background: linear-gradient(180deg, var(--art-tone), #e2e2e2);
    border-radius: 6px;
  }

  .brand-name {
    position: absolute;
    left: 40px;
    top: 378px;
    font-family: "Anton", sans-serif;
    font-size: 92px;
    line-height: 1;
    color: var(--ink);
    letter-spacing: -1px;
    z-index: 2;
  }

  .splash {
    position: absolute;
    left: 81px;
    top: 444px;
    width: 220px;
    height: 272px;
    background: var(--flavor);
    border-radius: 48% 52% 38% 44% / 40% 44% 56% 60%;
  }

  .no-sugar {
    position: absolute;
    left: 64px;
    top: 522px;
    width: 110px;
    height: 22px;
    background: var(--ink);
    color: #ffffff;
    border-radius: 11px;
    font-family: "Roboto Condensed", sans-serif;
    font-weight: 500;
    font-size: 15px;
    line-height: 22px;
    text-align: center;
    transform: rotate(-30deg);
    z-index: 2;
  }

  .flavor-name {
    position: absolute;
    left: 120px;
    top: 596px;
    width: 160px;
    font-family: "Oswald", sans-serif;
    font-weight: 400;
    font-size: 34px;
    line-height: 1;
    color: var(--ink);
    text-align: center;
    z-index: 2;
  }

  .stats {
    position: absolute;
    left: 0;
    top: 732px;
    width: 100%;
    text-align: center;
    font-family: "Roboto Condensed", sans-serif;
    color: var(--ink);
  }
  .stats__abv {
    display: inline-block;
    font-size: 19px;
    font-weight: 500;
    padding: 0 14px 2px;
    border-bottom: 1.5px solid var(--ink);
  }
  .stats__calories { font-size: 17px; margin-top: 4px; }
</style>
</head>
<body>
<main class="canvas">

  <section class="can can--orange" aria-label="VELKA Orange can label">
    <div class="band band--top"></div>
    <div class="scene-art" role="img" aria-label="Line drawing of mountain peaks, ski slope and a pine tree"></div>
    <div class="splash" role="img" aria-label="Orange juice splash"></div>
    <h1 class="brand-name">VELKA</h1>
    <div class="no-sugar">NO SUGAR</div>
    <p class="flavor-name">ORANGE</p>
    <div class="stats">
      <p class="stats__abv">5% alc/vol</p>
      <p class="stats__calories">ONLY 100 calories</p>
    </div>
    <div class="band band--bottom"></div>
  </section>

  <section class="can can--mango" aria-label="VELKA Mango can label">
    <div class="band band--top"></div>
    <div class="scene-art" role="img" aria-label="Line drawing of mountain peaks, ski slope and a pine tree"></div>
    <div class="splash" role="img" aria-label="Mango juice splash"></div>
    <h1 class="brand-name">VELKA</h1>
    <div class="no-sugar">NO SUGAR</div>
    <p class="flavor-name">MANGO</p>
    <div class="stats">
      <p class="stats__abv">5% alc/vol</p>
      <p class="stats__calories">ONLY 100 calories</p>
    </div>
    <div class="band band--bottom"></div>
  </section>

</main>
</body>
</html>
```